New Innovative Counselling and psychotherapy Service needs Business Card design

Keep it simple and professional. On one side, just company name and logo (perhaps in all blue) and maybe a tag line.

On other side (all white) my name and Qualifications in centre

Industry/Entity Type

Health And Wellness

Contact Information for Business Card

Derek Hollis
Counsellor & Psychotherapist
BSc (Psychol.), BA, Dip. (Couns. & Psych.), PG.Cert (CBT), MGVrA, NWTF

I will also require Mobile no, Email and web site address of which I'll pass on to final designer.

Font styles to use
Sans Serif

Requirements
Must have
• My Logo Only and please use the colours in logo that is in it.
Should not have
• Any other images

```html
<!DOCTYPE html>
<html lang="en">
<head>
<meta charset="utf-8">
<title>Harbor Lane – Business Card</title>
<link rel="stylesheet" href="https://fonts.googleapis.com/css2?family=Open+Sans:wght@300;400;600;700&display=swap">
<style>
  :root {
    --bg: #2b2b2b;
    --card: #ffffff;
    --blue: #3fb0ec;
    --green: #8cc63f;
    --ink: #4a4a4a;
    --muted: #7a7a7a;
    --rule: #d9d9d9;
  }
  * { margin: 0; padding: 0; box-sizing: border-box; }
  html, body {
    width: 1200px; height: 900px; overflow: hidden;
    background: var(--bg);
    font-family: "Open Sans", sans-serif;
  }
  .stage {
    width: 1200px; height: 900px;
    display: flex; flex-direction: column;
    align-items: center; justify-content: center; gap: 40px;
  }
  .card {
    position: relative;
    width: 700px; height: 400px;
    background: var(--card);
    overflow: hidden;
  }

  /* Front */
  .front {
    display: flex; flex-direction: column; align-items: center;
  }
  .front-mark {
    width: 130px; height: 130px; border-radius: 50%;
    background: var(--blue);
    margin-top: 62px;
  }
  .front-name {
    margin-top: 22px;
    font-size: 34px; font-weight: 300; color: var(--blue);
    letter-spacing: 0.5px;
  }
  .tagline {
    position: absolute; bottom: 52px; left: 0; right: 0;
    text-align: center;
    font-size: 17px; color: var(--muted); font-weight: 400;
  }

  /* Back */
  .brand {
    position: absolute; left: 62px; top: 150px;
    display: flex; align-items: center; gap: 14px;
  }
  .brand-dot {
    width: 46px; height: 46px; border-radius: 50%;
    background: var(--blue);
  }
  .brand-name {
    font-size: 30px; font-weight: 400; color: var(--ink);
  }
  .divider {
    position: absolute; left: 372px; top: 52px;
    width: 1px; height: 180px; background: var(--rule);
  }
  .details {
    position: absolute; left: 392px; top: 48px; width: 290px;
  }
  .person-name {
    font-size: 21px; font-weight: 700; color: var(--blue);
    text-transform: uppercase; line-height: 1.1;
  }
  .role {
    font-size: 15px; font-weight: 600; color: var(--green);
    text-transform: uppercase; margin-top: 2px;
  }
  .qualifications {
    font-size: 11.5px; color: var(--green); line-height: 1.35; margin-top: 4px;
  }
  .contact {
    list-style: none; margin-top: 10px;
  }
  .contact li {
    display: flex; align-items: center; gap: 8px;
    font-size: 14.5px; color: var(--ink); line-height: 1.5;
  }
  .contact svg { width: 14px; height: 14px; flex: none; }
  .band {
    position: absolute; left: 0; bottom: 0; width: 700px; height: 120px;
  }
  .website {
    position: absolute; left: 0; width: 560px; bottom: 18px;
    text-align: center;
    font-size: 19px; color: #ffffff; letter-spacing: 5px;
  }
  .band-dot {
    position: absolute; right: 22px; bottom: 66px;
    width: 38px; height: 38px; border-radius: 50%;
    background: #ffffff;
  }
</style>
</head>
<body>
<main class="stage">
  <section class="card front">
    <div class="front-mark"></div>
    <div class="front-name">Harbor Lane</div>
    <p class="tagline">Caring For Your Psychological Well-Being Is Our Top Priority</p>
  </section>

  <section class="card back">
    <div class="brand">
      <span class="brand-dot"></span>
      <span class="brand-name">Harbor Lane</span>
    </div>
    <div class="divider"></div>
    <div class="details">
      <h1 class="person-name">Derek Hollis</h1>
      <p class="role">Counsellor &amp; Psychotherapist</p>
      <p class="qualifications">BSc (Psychol.), BA, Dip. (Couns. &amp; Psych.)<br>PG.Cert (CBT), MGVrA, NWTF</p>
      <ul class="contact">
        <li>
          <svg viewBox="0 0 14 14" aria-hidden="true"><rect x="3" y="0.5" width="8" height="13" rx="1.5" fill="none" stroke="#3fb0ec" stroke-width="1.5"/><circle cx="7" cy="11" r="0.9" fill="#3fb0ec"/></svg>
          555 210 4417
        </li>
        <li>
          <svg viewBox="0 0 14 14" aria-hidden="true"><rect x="0.5" y="2.5" width="13" height="9" fill="#3fb0ec"/><path d="M0.5 2.5 L7 8 L13.5 2.5" fill="none" stroke="#ffffff" stroke-width="1.2"/></svg>
          derek@harborlane.com
        </li>
      </ul>
    </div>
    <svg class="band" viewBox="0 0 700 120" aria-hidden="true">
      <polygon points="0,62 580,62 700,22 700,120 0,120" fill="#3fb0ec"/>
    </svg>
    <span class="band-dot"></span>
    <p class="website">www.harborlane.com</p>
  </section>
</main>
</body>
</html>
```